VENTURE CAPITAL GROUP BUSINESS CARD DESIGN

Venture Capital Group based in SF looking for a bold business card design. No trendy colour explosion, 3D effects etc. Just "simple" optical effects. Works on your brain, keeps your eye focused and sticks to your mind.
Target Market(s)
Technology startups
Industry/Entity Type
Venture Capital
Contact Information for Business Card
BARNABY WHITLOCK
MANAGING PARTNER
817 FERN ST SAN FRANCISCO, CA 94111
415.555.0143 O
415.555.0167 F
415.555.0192 C
barn@halcyonridgefund.example

```html
<!DOCTYPE html>
<html lang="en">
<head>
<meta charset="utf-8">
<title>Halcyon Ridge Capital — Business Card</title>
<link href="https://fonts.googleapis.com/css2?family=Lato:wght@400;700;900&display=swap" rel="stylesheet">
<style>
  :root {
    --backdrop: #ece9e2;
    --card-white: #f1f1ef;
    --card-mint: #e6eedb;
    --green: #1f6e28;
    --green-deep: #155a1d;
    --green-line: #3c8a45;
    --charcoal: #2a2a2a;
    --charcoal-cell: #3a3a3a;
    --accent-green: #3fae4a;
    --white: #ffffff;
    --mark-grey: #d9d9d6;
  }
  * { box-sizing: border-box; margin: 0; padding: 0; }
  html, body { width: 1200px; height: 900px; overflow: hidden; }
  body {
    background: var(--backdrop);
    font-family: "Lato", Arial, sans-serif;
    position: relative;
  }
  .card {
    position: absolute;
    top: 135px;
    width: 360px;
    height: 630px;
    overflow: hidden;
    box-shadow: 0 12px 30px rgba(0,0,0,.12);
  }
  .card--front { left: 180px; background: var(--card-white); }
  .card--back  { left: 660px; background: var(--card-mint); }

  .tab {
    position: absolute;
    height: 12px;
    background: var(--green);
  }
  .tab--top { top: 0; left: 70px; width: 200px; clip-path: polygon(0 0,100% 0,96% 100%,4% 100%); }
  .tab--bottom { bottom: 0; left: 90px; width: 200px; clip-path: polygon(4% 0,96% 0,100% 100%,0 100%); }

  .brand {
    position: absolute;
    left: 0; right: 0;
    display: flex;
    flex-direction: column;
    align-items: center;
    gap: 20px;
  }
  .card--front .brand { top: 200px; }
  .card--back .brand { top: 70px; }
  .brand__dot {
    width: 110px; height: 110px;
    border-radius: 50%;
    background: var(--mark-grey);
  }
  .brand__name {
    font-weight: 700;
    font-size: 22px;
    letter-spacing: 1.5px;
    color: var(--green);
    text-align: center;
  }

  .person {
    position: absolute;
    top: 298px; left: 0; right: 0;
    height: 58px;
    background: var(--charcoal);
    padding: 10px 0 0 94px;
  }
  .person__name { color: var(--white); font-weight: 900; font-size: 18px; letter-spacing: .5px; }
  .person__title { color: var(--accent-green); font-weight: 900; font-size: 11px; letter-spacing: 1px; margin-top: 2px; }

  .contact {
    position: absolute;
    top: 356px; left: 0; right: 0; bottom: 0;
    background: var(--green);
    list-style: none;
  }
  .contact__row {
    display: flex;
    align-items: center;
    border-bottom: 1px solid var(--green-line);
  }
  .contact__row:nth-child(1) { height: 86px; }
  .contact__row:nth-child(2) { height: 68px; }
  .contact__row:nth-child(3) { height: 68px; }
  .contact__row:nth-child(4) { height: 52px; border-bottom: none; }
  .contact__icon {
    width: 70px; height: 100%;
    flex-shrink: 0;
    display: flex; align-items: center; justify-content: center;
    background: var(--green-deep);
    border-right: 1px solid var(--green-line);
  }
  .contact__row:nth-child(1) .contact__icon { background: var(--charcoal-cell); }
  .contact__text {
    padding-left: 24px;
    color: var(--white);
    font-size: 13px;
    line-height: 1.35;
    letter-spacing: .3px;
  }
</style>
</head>
<body>

<section class="card card--front" aria-label="Card front">
  <div class="tab tab--top"></div>
  <div class="brand">
    <span class="brand__dot"></span>
    <span class="brand__name">HALCYON RIDGE CAPITAL</span>
  </div>
  <div class="tab tab--bottom"></div>
</section>

<section class="card card--back" aria-label="Card back">
  <div class="tab tab--top"></div>
  <div class="brand">
    <span class="brand__dot"></span>
    <span class="brand__name">HALCYON RIDGE CAPITAL</span>
  </div>

  <div class="person">
    <p class="person__name">BARNABY WHITLOCK</p>
    <p class="person__title">MANAGING PARTNER</p>
  </div>

  <ul class="contact">
    <li class="contact__row">
      <span class="contact__icon">
        <svg width="24" height="24" viewBox="0 0 24 24" fill="#fff"><circle cx="12" cy="8" r="5"/><path d="M3 22c0-5 4-8 9-8s9 3 9 8z"/></svg>
      </span>
      <p class="contact__text">555.555.0143 O<br>555.555.0167 F<br>555.555.0192 C</p>
    </li>
    <li class="contact__row">
      <span class="contact__icon">
        <svg width="18" height="26" viewBox="0 0 18 26" fill="none" stroke="#fff" stroke-width="2"><rect x="2" y="1" width="14" height="24" rx="2"/><line x1="7" y1="21" x2="11" y2="21"/></svg>
      </span>
      <p class="contact__text">barn@halcyonridgefund.example</p>
    </li>
    <li class="contact__row">
      <span class="contact__icon">
        <svg width="24" height="24" viewBox="0 0 24 24" fill="none" stroke="#fff" stroke-width="1.6"><circle cx="12" cy="12" r="10"/><ellipse cx="12" cy="12" rx="4.5" ry="10"/><line x1="2" y1="12" x2="22" y2="12"/><line x1="4" y1="6.5" x2="20" y2="6.5"/><line x1="4" y1="17.5" x2="20" y2="17.5"/></svg>
      </span>
      <p class="contact__text">817 FERN ST BRAMBLEWICK,<br>ST 00417</p>
    </li>
    <li class="contact__row">
      <span class="contact__icon">
        <svg width="24" height="22" viewBox="0 0 24 22" fill="#fff"><path d="M12 1 1 11h3v10h6v-6h4v6h6V11h3z"/></svg>
      </span>
    </li>
  </ul>
</section>

</body>
</html>
```